Business card design for a dynamic IT consulting company

We need a business card design for a young firm, specialized in the Telecommunications/Consulting industry. The name of the company is Dulmar and Partners Business Consulting Ltd. (Short name: Dulmar and Partnes)
Dulmar = solve read reverse, so we aim to be uncomplicated and solution-oriented. The small pipe in our logo is also related to the word solve. So we need a new business card design, which is simple, eye catching and something non traditional (I would probably prefer a square shaped design rather than a rectangle, but open for suggestions). Attached our logo.

Target Market(s)

Usually our customers are Tier1 Telecoms providers (Q-Linkor, Teravine, etc) and their executives.

Industry/Entity Type

Business

Contact Information for Business Card

Name: Gergely Tarnavedi
Email: g.tarnavedi@dulmar-example.hu
Web: www.dulmar-example.hu
Mobile: +36 30 555 0192
Title: Managing Director

Optional:
Company name: Dulmar and Partners Ltd.
Address: 1021 Budapest, Kovarhegyi str. 17/B, Hungary

Font styles to use
Other font styles liked:
• helveticaneue_medium, Prime Regular are used now.

Colors

Designer to choose colors to be used in the design.

Requirements
Must have
• I would like to have a 2 sided design.
Nice to have
• I thought if we make the logo a bit bigger (without the company name), that could go to the back with the company name below. I though, if the pipe in the logo is somehow touchable on the business card, would be nice and unique.

```html
<!DOCTYPE html>
<html lang="en">
<head>
<meta charset="utf-8">
<title>Dulmar and Partners – Business Card</title>
<link rel="stylesheet" href="https://fonts.googleapis.com/css2?family=Roboto:wght@400;500;700&display=swap">
<style>
  :root {
    --stage: #1a1a1c;
    --card-dark: #2a2a2c;
    --card-dark-deep: #1e1e20;
    --card-light: #f2f2f3;
    --accent-blue: #2b9fd8;
    --accent-magenta: #c9349f;
    --accent-gray: #7a7a7c;
    --text-gray: #5a5a5c;
    --logo-light: #e4e4e6;
    --rule: #a8a8aa;
  }
  * { margin: 0; padding: 0; box-sizing: border-box; }
  html, body {
    width: 1200px; height: 900px; overflow: hidden;
    background: var(--stage);
    font-family: "Roboto", Arial, sans-serif;
  }
  .stage { position: relative; width: 1200px; height: 900px; }
  .card {
    position: absolute; left: 280px;
    width: 640px; height: 366px;
    border-radius: 16px; overflow: hidden;
    box-shadow: 0 14px 34px rgba(0,0,0,.55);
  }
  .card--front { top: 70px; background: var(--card-light); }
  .card--back {
    top: 464px;
    background: linear-gradient(160deg, var(--card-dark) 0%, var(--card-dark-deep) 100%);
  }

  /* front */
  .front-band {
    position: absolute; left: 0; top: 0; width: 100%; height: 136px;
    background: linear-gradient(160deg, #333335 0%, var(--card-dark) 100%);
  }
  .front-stripes {
    position: absolute; left: 0; top: 136px; width: 100%; height: 6px; display: flex;
  }
  .stripe--blue { width: 290px; background: var(--accent-blue); }
  .stripe--magenta { width: 200px; background: var(--accent-magenta); }
  .stripe--gray { flex: 1; background: var(--accent-gray); }

  .brand {
    position: absolute; display: flex; align-items: center; gap: 12px;
    font-weight: 500; color: var(--logo-light); letter-spacing: .5px;
    white-space: nowrap;
  }
  .brand__mark { width: 18px; height: 18px; background: var(--accent-magenta); }
  .front-band .brand { right: 44px; top: 52px; font-size: 32px; }

  .contact { position: absolute; left: 40px; top: 166px; right: 40px; }
  .contact__name { font-size: 28px; font-weight: 700; line-height: 1.1; }
  .contact__first { color: var(--accent-blue); }
  .contact__last { color: var(--accent-magenta); }
  .contact__title { font-size: 15px; color: var(--text-gray); margin-top: 4px; }
  .contact__company { font-size: 14px; font-weight: 500; color: var(--accent-blue); margin-top: 16px; }
  .contact__address { font-size: 14px; color: var(--text-gray); margin-top: 3px; }
  .contact__rule { height: 1px; background: var(--rule); margin: 14px 0 12px; }
  .contact__row {
    display: flex; justify-content: space-between; align-items: center;
    font-size: 14px; color: var(--text-gray); white-space: nowrap;
  }
  .contact__item { display: flex; align-items: center; gap: 7px; }
  .icon { width: 20px; height: 20px; border-radius: 3px; display: block; flex: none; }

  /* back */
  .card--back .brand {
    left: 50%; top: 138px; transform: translateX(-50%);
    font-size: 44px;
  }
  .card--back .brand__mark { width: 24px; height: 24px; }
  .back-url {
    position: absolute; left: 0; right: 0; top: 236px; text-align: center;
    font-size: 14px; color: var(--accent-gray); letter-spacing: .5px;
  }
</style>
</head>
<body>
<main class="stage">

  <section class="card card--front" aria-label="Business card front">
    <div class="front-band">
      <div class="brand"><span class="brand__mark"></span><span class="brand__name">Dulmar &amp; Partners</span></div>
    </div>
    <div class="front-stripes">
      <span class="stripe--blue"></span><span class="stripe--magenta"></span><span class="stripe--gray"></span>
    </div>

    <div class="contact">
      <h1 class="contact__name"><span class="contact__first">Gergely</span> <span class="contact__last">Tarnavedi</span></h1>
      <p class="contact__title">Managing Director</p>
      <p class="contact__company">Dulmar and Partners Ltd</p>
      <p class="contact__address">1021 Budapest, Kovarhegyi str. 17/B, Hungary</p>
      <div class="contact__rule"></div>
      <div class="contact__row">
        <span class="contact__item">
          <svg class="icon" viewBox="0 0 20 20" aria-hidden="true">
            <rect width="20" height="20" rx="3" fill="#2b9fd8"/>
            <path d="M6.5 4.5c.6-.4 1.3 0 1.6.6l.8 1.7c.2.5.1 1-.3 1.3l-.8.6c.6 1.4 1.6 2.4 3 3l.6-.8c.3-.4.8-.5 1.3-.3l1.7.8c.6.3 1 1 .6 1.6-.5.9-1.5 1.6-2.6 1.4-3.6-.6-6.4-3.4-7-7-.2-1.1.5-2.1 1.1-2.9z" fill="#fff"/>
          </svg>
          +36 30 555 0192
        </span>
        <span class="contact__item">
          <svg class="icon" viewBox="0 0 20 20" aria-hidden="true">
            <rect width="20" height="20" rx="3" fill="#c9349f"/>
            <rect x="4" y="6" width="12" height="8" fill="none" stroke="#fff" stroke-width="1.4"/>
            <path d="M4 6l6 5 6-5" fill="none" stroke="#fff" stroke-width="1.4"/>
          </svg>
          g.tarnavedi@dulmar-example.hu
        </span>
        <span class="contact__item">
          <svg class="icon" viewBox="0 0 20 20" aria-hidden="true">
            <rect width="20" height="20" rx="3" fill="#7a7a7c"/>
            <circle cx="10" cy="10" r="5.5" fill="none" stroke="#fff" stroke-width="1.3"/>
            <path d="M4.5 10h11M10 4.5c-2 2.8-2 8.2 0 11M10 4.5c2 2.8 2 8.2 0 11" fill="none" stroke="#fff" stroke-width="1.1"/>
          </svg>
          www.dulmar-example.hu
        </span>
      </div>
    </div>
  </section>

  <section class="card card--back" aria-label="Business card back">
    <div class="brand"><span class="brand__mark"></span><span class="brand__name">Dulmar &amp; Partners</span></div>
    <p class="back-url">www.dulmar-example.hu</p>
  </section>

</main>
</body>
</html>
```